Morvina - A new California agave spirit brand needs a label!

Hello designers! We had a lot of fun with our last project getting our logo design, now we need to put that logo onto a label!

Morvina is a company that makes agave spirit (aka Tequila but we can't call it that because of regional laws) from California grown agaves. Our goal is to make a premium quality that goes head to head with some of the best tequilas in the world, and we need a package that conveys that.

The label that we want will be sophisticated and bold that will stand out on a shelf and be recognizable from across a bar. It needs to convey its premium status just from a glance.

Please do not use colors other than white, black, and sky/electric blue. The color scheme I see most likely winning will be some sort of white/offwhite background with black lettering, with possibly an accent of blue.

I will supply the winning logo artwork from the last contest, but if you have a better logo in mind feel free to create something new.

Please look at the link provided below for examples of the highest rated blanco tequilas.

https://www.spiritfinderhub.example/agave_spirits/blanco?q=&hPP=30&idx=BaseProduct&p=0&dFR%5Bcategory%5D%5B0%5D=Blanco

Please reference the QRL documents attached on mandatory label requirements.
Use this link for descriptions of each element of an alcohol label: https://www.qrlbureau.example/ds-labeling-home/anatomy-of-a-distilled-spirits-label-tool

Our label must have these elements:

Brand Name: Morvina
Class/Type Description: California Agave Spirit
Fanciful Name: Blanco
Alcohol Content: 40% ABV
Government Warning
Name and Address: Distilled and Bottled by Morvina Spirits, Durham, CA
Net Contents: 750 ml
Barcode
Website: www.morvinaspirits.example
Please leave a space for a brief paragraph on the back of the bottle

Thank you and good luck!

Target Market(s)

Premium Tequila Drinkers

Industry/Entity Type

Distilled Spirits

Colors

Designer to choose colors to be used in the design.

Requirements
Must have
• Please reference the QRL documents provided on required label information.

```html
<!DOCTYPE html>
<html lang="en">
<head>
<meta charset="utf-8">
<title>Morvina California Agave Spirit – Blanco Label</title>
<link rel="stylesheet" href="https://fonts.googleapis.com/css2?family=Oswald:wght@600;700&family=Jost:wght@400;500&display=swap">
<style>
  :root {
    --page: #f5f6f7;
    --silver-light: #e6e7e9;
    --silver-mid: #d2d3d6;
    --silver-dark: #bfc1c4;
    --sky: #c3d5f0;
    --sky-deep: #93acd2;
    --ink: #111214;
    --tag: #a9bbd6;
  }
  * { margin: 0; padding: 0; box-sizing: border-box; }
  html, body {
    width: 1200px; height: 1200px; overflow: hidden;
    background: var(--page);
  }
  .canvas { position: relative; width: 1200px; height: 1200px; }

  /* Neck band */
  .neck-band {
    position: absolute; left: 420px; top: 96px;
    width: 300px; height: 76px;
    background: linear-gradient(180deg, var(--silver-light) 0%, var(--sky) 100%);
    display: flex; align-items: center; justify-content: center;
  }
  .neck-band__text {
    font-family: "Oswald", sans-serif; font-weight: 700;
    font-size: 50px; line-height: 1; color: var(--ink);
    letter-spacing: 0.5px;
  }
  .neck-tag {
    position: absolute; left: 720px; top: 88px;
    width: 96px; height: 96px; background: var(--tag);
    display: flex; align-items: center; justify-content: center;
  }
  .neck-tag__mark {
    width: 54px; height: 54px; border-radius: 50%;
    border: 3px solid var(--ink);
  }

  /* Front label */
  .front-label {
    position: absolute; left: 380px; top: 250px;
    width: 440px; height: 880px;
    border-radius: 220px;
    overflow: hidden;
    background: linear-gradient(160deg, var(--silver-light) 0%, var(--silver-mid) 40%, var(--silver-dark) 100%);
  }
  .front-label__art {
    position: absolute; left: 0; right: 0; top: 230px; bottom: 0;
    background: linear-gradient(180deg, rgba(195,213,240,0) 0%, var(--sky) 14%, var(--sky-deep) 100%);
  }
  .front-label__content {
    position: absolute; inset: 0;
    display: flex; flex-direction: column; align-items: center;
    color: var(--ink); text-align: center;
  }
  .brand { margin-top: 112px; display: flex; flex-direction: column; align-items: center; }
  .brand__mark {
    width: 64px; height: 64px; border-radius: 50%;
    border: 3px solid var(--ink);
  }
  .brand__name {
    margin-top: 14px;
    font-family: "Jost", sans-serif; font-weight: 400;
    font-size: 32px; letter-spacing: 4px; line-height: 1;
  }
  .class-type {
    margin-top: 40px;
    font-family: "Oswald", sans-serif; font-weight: 700;
    text-transform: uppercase; line-height: 0.98;
  }
  .class-type__region { display: block; font-size: 70px; letter-spacing: 0.5px; }
  .class-type__main { display: block; font-size: 126px; letter-spacing: 1px; }
  .fanciful {
    margin-top: 20px;
    font-family: "Jost", sans-serif; font-weight: 500;
    font-size: 30px; letter-spacing: 7px; line-height: 1;
  }
  .producer {
    margin-top: 24px;
    font-family: "Jost", sans-serif; font-weight: 400;
    font-size: 18px; letter-spacing: 4.5px; line-height: 1.45;
    text-transform: uppercase;
  }
  .contents {
    margin-top: 18px;
    font-family: "Oswald", sans-serif; font-weight: 600;
    font-size: 18px; letter-spacing: 0.3px;
  }
</style>
</head>
<body>
<main class="canvas">

  <div class="neck-band">
    <span class="neck-band__text">AGAVE SPIRIT</span>
  </div>
  <div class="neck-tag"><span class="neck-tag__mark"></span></div>

  <section class="front-label">
    <div class="front-label__art" role="img" aria-label="Illustration of California mountains with agave plants in the foreground"></div>

    <div class="front-label__content">
      <div class="brand">
        <span class="brand__mark"></span>
        <span class="brand__name">MORVINA</span>
      </div>
      <h1 class="class-type">
        <span class="class-type__region">California</span>
        <span class="class-type__main">Agave</span>
        <span class="class-type__main">Spirit</span>
      </h1>
      <p class="fanciful">BLANCO</p>
      <p class="producer">Distilled and bottled<br>by Morvina Spirits<br>Durham, CA</p>
      <p class="contents">40% ABV | 750 ML</p>
    </div>
  </section>

</main>
</body>
</html>
```